Wesbite design for Investment Firm

We want a basic (clean) website that follows the form, fonts and colors of our attachments. This is for a financial investment management firm, but we have a boutique (anti-Wall Street) approach. Site should have an Home Page (Logo up top - room for basic copy on bottom, Philosophy Page (room for Quarterly Letter attachment and basic copy, Performance Page (room for Performance Overview and Performance Analysis and basic copy), Team Page, Commentary Page and Contact
Updates

Reason: Some designers have asked for an extension. Again, please only use image of Train Station or Train Station Logo in design.

Target Market(s)

Small and mid-size financial advisors from across the country

Industry/Entity Type

Financial

Number of Pages Required

5+ page

Font styles to use
Other font styles liked:
• Palotino Linotype

Colors
3176b5
cfdeed
ffffff

Requirements
Must have
• Please refer to existing site www.qarvelton.com. Of note, this is too complex / cluttered. We simply want Blur, Grey and White consistent with attachments. The copy is pretty good, but will be simplified (and no quotes)
Should not have
• No images other than train station logo and / or train station image

```html
<!DOCTYPE html>
<html lang="en">
<head>
<meta charset="utf-8">
<title>Ashford Lane Investment Company</title>
<link rel="stylesheet" href="https://fonts.googleapis.com/css2?family=Cormorant+Garamond:wght@500;600&family=Gentium+Book+Plus&family=Roboto:wght@300;400&display=swap">
<style>
  :root {
    --brand-blue: #3176b5;
    --pale-blue: #cfdeed;
    --mid-blue: #8fb3da;
    --white: #ffffff;
    --ink: #1c1c1c;
    --grey-text: #3a3a3a;
    --rule: #e2e2e2;
  }
  * { margin: 0; padding: 0; box-sizing: border-box; }
  html, body {
    width: 1200px;
    height: 886px;
    overflow: hidden;
    background: var(--white);
  }
  .page {
    position: relative;
    width: 1200px;
    height: 886px;
  }
  .site-name {
    position: absolute;
    top: 26px;
    left: 0;
    width: 100%;
    text-align: center;
    font-family: "Cormorant Garamond", serif;
    font-weight: 600;
    font-size: 29px;
    letter-spacing: 4px;
    text-transform: uppercase;
    color: var(--ink);
  }
  .main-nav {
    position: absolute;
    top: 88px;
    left: 0;
    width: 100%;
  }
  .main-nav ul { list-style: none; }
  .main-nav li {
    position: absolute;
    transform: translateX(-50%);
    font-family: "Gentium Book Plus", serif;
    font-size: 20px;
    color: var(--ink);
    white-space: nowrap;
  }
  .main-nav li.is-current { color: var(--brand-blue); }
  .nav-divider {
    position: absolute;
    top: 5px;
    width: 1px;
    height: 20px;
    background: var(--rule);
  }
  .hero-scene {
    position: absolute;
    left: 184px;
    top: 128px;
    width: 830px;
    height: 482px;
    border-radius: 50% 50% 48% 52% / 60% 55% 45% 40%;
    background: radial-gradient(ellipse at 60% 50%, var(--mid-blue) 0%, var(--pale-blue) 45%, rgba(207,222,237,0.35) 75%, rgba(255,255,255,0) 100%);
  }
  .intro {
    position: absolute;
    top: 636px;
    left: 0;
    width: 100%;
    text-align: center;
  }
  .intro h1 {
    font-family: "Gentium Book Plus", serif;
    font-weight: 400;
    font-size: 25px;
    color: var(--brand-blue);
    margin-bottom: 18px;
  }
  .intro p {
    width: 900px;
    margin: 0 auto 6px;
    font-family: "Roboto", sans-serif;
    font-weight: 300;
    font-size: 14.5px;
    line-height: 26px;
    color: var(--grey-text);
  }
  .intro strong {
    font-weight: 400;
    color: var(--ink);
  }
  .site-footer {
    position: absolute;
    top: 844px;
    left: 0;
    width: 100%;
    text-align: center;
    font-family: "Roboto", sans-serif;
    font-weight: 300;
    font-size: 13px;
    color: var(--grey-text);
  }
</style>
</head>
<body>
<div class="page">
  <header>
    <div class="site-name">Ashford Lane Investment Company</div>
    <nav class="main-nav">
      <ul>
        <li class="is-current" style="left:160px">Home</li>
        <li style="left:327px">Our Philosophy</li>
        <li style="left:521px">Performance</li>
        <li style="left:692px">Our Team</li>
        <li style="left:866px">Commentary</li>
        <li style="left:1028px">Contact</li>
      </ul>
      <span class="nav-divider" style="left:224px"></span>
      <span class="nav-divider" style="left:431px"></span>
      <span class="nav-divider" style="left:613px"></span>
      <span class="nav-divider" style="left:773px"></span>
      <span class="nav-divider" style="left:959px"></span>
    </nav>
  </header>

  <div class="hero-scene" role="img" aria-label="Blue pencil sketch of a small railway station with a train at the platform and a picket fence"></div>

  <main class="intro">
    <h1>We Are A Financial Investment Management Firm</h1>
    <p>At Ashford Lane, we employ an absolute return mindset to long only value investing. As fundamentally focused equity investors, we seek to identify good business models with high barriers to entry trading at substantial discounts to our conservative estimate of fair value. Finally, we contend that <strong>entry price is a significant determinant of return.</strong></p>
    <p>We ignore Wall Street research and our approach is not constrained by market size. Our <strong>independence, patience</strong> and <strong>clearly defined process</strong> drive the investment returns we seek for ourselves and our clients.</p>
  </main>

  <footer class="site-footer">Copyright © 2017&nbsp; Ashford Lane Investment Company.&nbsp; All Right Reserved.</footer>
</div>
</body>
</html>
```